Stationery Design Project

Hi All,

We need you to design stationary for a new Business and Accounting Advisory Firm. We have already got the logo designed and it is attached. If you could also if possible, match the fonts in your design to that on the logo’s provided.

What we need:
- Business Card
- A4 Letter head
- A4 Folders
- PPT template (Title page and regular page)

And what ever else you want to throw in.

We are in the process of getting the web site designed, however below is a list of websites which we like which will give you an understanding of the style that we are going for.

- plavoni.com
- brightfunnelo.com
- hourquillet.com
- artmarrowly.com

I look forward to your seeing your design.

Hi All,

I have just realised that I forgot that i need to include a Licensed Tallymasters image on the letter head, please find attaced as File 1. Could you please have this image in the bottom left header.

Regards,

Gareth

Industry/Entity Type

Business

Requirements
Must have
• Outputs:
- Documents ready to print
- Generic editable information
- Pdf copies of the documents
- Word version of letterhead

```html
<!DOCTYPE html>
<html lang="en">
<head>
<meta charset="utf-8">
<title>Brannock Partners – Letterhead</title>
<link rel="stylesheet" href="https://fonts.googleapis.com/css2?family=EB+Garamond:wght@500&family=Open+Sans:wght@400&family=Roboto:wght@700&display=swap">
<style>
  :root {
    --brand-blue: #3a5ca6;
    --brand-navy: #2f4e96;
    --brand-cyan: #3db8e2;
    --brand-orange: #f7941d;
    --brand-amber: #fbb03b;
    --badge-red: #c4202e;
    --ink-black: #111111;
    --paper: #ffffff;
  }
  html, body {
    margin: 0;
    padding: 0;
    overflow: hidden;
    background: var(--paper);
  }
  .letterhead {
    position: relative;
    width: 927px;
    height: 1200px;
    background: var(--paper);
    overflow: hidden;
  }
  .brand {
    position: absolute;
    left: 62px;
    top: 48px;
    display: flex;
    align-items: center;
    gap: 22px;
  }
  .brand-dot {
    width: 100px;
    height: 100px;
    border-radius: 50%;
    background: var(--brand-cyan);
    flex: none;
  }
  .brand-name {
    margin: 0;
    font-family: "EB Garamond", serif;
    font-weight: 500;
    font-size: 50px;
    line-height: 1;
    color: var(--brand-blue);
  }
  .brand-tagline {
    margin: 8px 0 0 2px;
    font-family: "Open Sans", sans-serif;
    font-size: 18px;
    letter-spacing: 0.62em;
    color: var(--brand-blue);
  }
  .contact {
    position: absolute;
    left: 718px;
    top: 62px;
    font-family: "Open Sans", sans-serif;
    font-size: 14px;
    line-height: 19px;
    color: var(--brand-blue);
  }
  .contact p { margin: 0 0 11px; }
  .footer {
    position: absolute;
    left: 0;
    right: 0;
    top: 1126px;
    height: 60px;
  }
  .accreditation {
    position: absolute;
    left: 20px;
    top: 2px;
    display: flex;
    align-items: center;
    gap: 14px;
  }
  .accreditation-badge {
    width: 56px;
    height: 56px;
    border-radius: 50%;
    background: var(--badge-red);
  }
  .accreditation-label {
    font-family: "Roboto", sans-serif;
    font-weight: 700;
    font-size: 17px;
    line-height: 18px;
    color: var(--ink-black);
  }
  .rule {
    position: absolute;
    top: 28px;
    height: 6px;
  }
  .rule-blue {
    left: 201px;
    width: 342px;
    background: linear-gradient(90deg, var(--brand-cyan), var(--brand-navy));
  }
  .rule-orange {
    left: 783px;
    width: 144px;
    background: linear-gradient(90deg, var(--brand-orange), var(--brand-amber));
  }
  .website {
    position: absolute;
    left: 559px;
    top: 19px;
    font-family: "Open Sans", sans-serif;
    font-size: 17px;
    color: var(--brand-blue);
  }
</style>
</head>
<body>
  <main class="letterhead">
    <header>
      <div class="brand">
        <span class="brand-dot" aria-hidden="true"></span>
        <div>
          <h1 class="brand-name">Brannock Partners</h1>
          <p class="brand-tagline">Business Advisors</p>
        </div>
      </div>
      <address class="contact" style="font-style: normal;">
        <p>1234 Street Address<br>City, State 12345</p>
        <p>P: (123) 456-7890<br>F: (123) 987-6543</p>
      </address>
    </header>
    <footer class="footer">
      <div class="accreditation">
        <span class="accreditation-badge" aria-hidden="true"></span>
        <span class="accreditation-label">Licensed<br>Tallymaster</span>
      </div>
      <span class="rule rule-blue" aria-hidden="true"></span>
      <span class="website">www.brannockpartners.com</span>
      <span class="rule rule-orange" aria-hidden="true"></span>
    </footer>
  </main>
</body>
</html>
```